Skill Up Salary Up

Full Page
7.5 w x 10 h / 8 w x 10.75 h + .25" bleed
Full-Page Career Course Ad
Project Overview
• Goal: Create a visually attractive, modern, and uncluttered full-page magazine advertisement to list available career courses.
• Tone: Creative, professional, and attention-grabbing to prevent the reader from turning the page. The final design must prioritize readability.

Content Requirements
1. Header/Headline: Must be the primary focus. And grab peoples attention
2. Course Listing: A clear, well-organized list of the career courses.
________________________________________
Design & Aesthetic Directives
1. Layout & Readability (Crucial)
• The final ad must not look crowded or busy.
• Prioritize white space to make the text "breathe" and ensure the course list is easy to scan and read.
• Use a modern, clean, and professional typeface (font choice is critical for the aesthetic).
2. Visual Style
• Aim for a creative, modern, and fresh look. Avoid outdated or generic stock imagery/layouts.
3. Imagery/Graphic Element (Artist's Choice)
You have creative freedom regarding the main graphic element.
• Option A (Photography): Use a photo of a white male American with a collared shirt. The imagery should convey success, focus, or professional development.
• Option B (Vector/Illustration): Use a modern vector graphic, illustration, or abstract design. This could be used to symbolize growth, connection, or a career path.
The choice of graphic element is yours, but it must support the overall modern and uncrowded aesthetic.

Requirements
Must have
• Partial listing .. is part of the Vocational Horizon Course

```html
<!DOCTYPE html>
<html lang="en">
<head>
<meta charset="utf-8">
<title>Skill Up, Salary Up – Vocational Horizon Course</title>
<link rel="stylesheet" href="https://fonts.googleapis.com/css2?family=Inter:ital,wght@0,300;0,400;0,700;0,800;0,900;1,900&display=swap">
<style>
  :root {
    --ink: #0b0b0b;
    --paper: #ffffff;
    --sky-1: #ffffff;
    --sky-2: #e6f1f8;
    --sky-3: #cfe2ee;
    --rule: #8a8a8a;
  }
  * { margin: 0; padding: 0; box-sizing: border-box; }
  html, body { width: 893px; height: 1200px; overflow: hidden; background: var(--paper); }
  body { font-family: "Inter", Arial, sans-serif; color: var(--ink); }

  .ad { position: relative; width: 893px; height: 1200px; overflow: hidden; background: var(--paper); border: 1px solid var(--ink); }

  .hero-bg {
    position: absolute; left: 0; top: 0; width: 893px; height: 550px;
    background: linear-gradient(180deg, var(--sky-2) 0%, var(--sky-1) 55%, var(--sky-1) 100%);
  }
  .hero-photo {
    position: absolute; left: 300px; top: 0; width: 593px; height: 550px;
    background:
      radial-gradient(ellipse 45% 60% at 75% 50%, #e9e6e3 0%, rgba(233,230,227,0) 70%),
      linear-gradient(160deg, var(--sky-2) 0%, var(--sky-3) 40%, #f4f7f9 85%, var(--sky-1) 100%);
  }

  .headline { position: absolute; left: 84px; top: 50px; }
  .headline-title { font-weight: 900; font-style: italic; font-size: 44px; letter-spacing: -1px; line-height: 1; }
  .headline-sub { font-weight: 400; font-size: 30px; letter-spacing: 0.3px; margin-top: 6px; }

  .goals {
    position: absolute; left: 0; top: 146px; width: 560px; height: 80px;
    background: var(--ink); color: var(--paper);
    clip-path: polygon(0 0, 100% 0, 100% 75%, 540px 100%, 0 100%);
  }
  .goal { position: absolute; top: 22px; font-size: 17px; font-weight: 500; letter-spacing: 0.6px; line-height: 21px; }
  .goal-1 { left: 84px; } .goal-2 { left: 257px; } .goal-3 { left: 409px; }
  .goal-divider { position: absolute; top: 0; width: 2px; height: 80px; background: var(--paper); }

  .listing { position: absolute; left: 84px; top: 245px; width: 480px; font-size: 15px; line-height: 20px; letter-spacing: 0.5px; }
  .listing strong { font-weight: 800; }

  .badge { position: absolute; left: 84px; top: 330px; width: 196px; height: 176px; }
  .badge svg { position: absolute; inset: 0; }
  .badge-text { position: absolute; inset: 0; color: var(--paper); text-align: center; transform: rotate(-3deg); padding-top: 27px; }
  .badge-span { font-size: 20px; line-height: 22px; }
  .badge-unit { font-size: 22px; line-height: 24px; }
  .badge-month { font-size: 44px; font-weight: 900; line-height: 44px; }
  .badge-year { font-size: 28px; font-weight: 800; line-height: 30px; }

  .courses { position: absolute; left: 49px; top: 562px; width: 795px; height: 426px; }
  .course { position: absolute; top: 0; height: 426px; }
  .course-1 { left: 0; width: 190px; }
  .course-2 { left: 218px; width: 190px; }
  .course-3 { left: 422px; width: 190px; }
  .course-4 { left: 626px; width: 170px; }
  .course-divider { position: absolute; top: 4px; width: 1px; height: 422px; background: var(--rule); }

  .course-title { font-size: 27px; font-weight: 800; line-height: 31px; letter-spacing: -0.2px; }
  .course-tag { font-size: 18px; font-weight: 800; line-height: 22px; margin-top: 12px; }
  .course-tag small { display: block; font-size: 15px; line-height: 22px; }
  .course-note { font-size: 15px; font-weight: 800; line-height: 18px; margin-top: 8px; }
  .ticks { list-style: none; margin-top: 16px; font-size: 15px; line-height: 18px; letter-spacing: 0.3px; }
  .ticks li { position: relative; padding-left: 14px; margin-bottom: 7px; }
  .ticks li::before { content: "\2713"; position: absolute; left: 0; top: 0; }
  .ticks.tight { margin-top: 0; }
  .ticks.tight li { margin-bottom: 7.5px; }
  .optional { position: absolute; top: 324px; font-size: 15px; line-height: 19px; }
  .optional strong { font-weight: 800; }
  .lab { position: absolute; top: 292px; font-size: 15px; font-weight: 800; line-height: 18px; }
  .duration { position: absolute; bottom: 0; font-size: 28px; font-weight: 800; line-height: 31px; white-space: nowrap; }

  .rule { position: absolute; left: 49px; width: 795px; height: 1px; background: var(--rule); }
  .closing { position: absolute; left: 0; top: 1005px; width: 893px; text-align: center; }
  .closing-kicker { font-size: 27px; font-weight: 300; letter-spacing: 1px; line-height: 30px; }
  .closing-title { font-size: 27px; font-weight: 900; line-height: 28px; }
  .closing-facts { font-size: 15px; font-weight: 400; letter-spacing: 0.3px; margin-top: 8px; word-spacing: 1px; }
  .closing-facts span { margin: 0 12px; }
</style>
</head>
<body>
<main class="ad">
  <div class="hero-bg"></div>
  <div class="hero-photo" role="img" aria-label="Photo of a smiling professional man in a white collared shirt and striped tie, holding glasses, seated at a laptop in a bright office"></div>

  <header class="headline">
    <h1 class="headline-title">Vocational Horizon</h1>
    <p class="headline-sub">Business Skills &amp; Knowledge to:</p>
  </header>

  <div class="goals">
    <div class="goal goal-1">Impress your<br>interviewer</div>
    <div class="goal-divider" style="left:220px"></div>
    <div class="goal goal-2">Maximize<br>Income</div>
    <div class="goal-divider" style="left:373px"></div>
    <div class="goal goal-3">Start / Run<br>Your Business</div>
  </div>

  <p class="listing"><strong>PARTIAL LISTING</strong> Computers / Marketing / Sales / Finance / Healthcare / Business Strategy /Communication / LedgerPro / Investments / Real Estate / Accounting</p>

  <div class="badge">
    <svg width="196" height="176" viewBox="0 0 196 176">
      <polygon points="43,8 140,1 193,81 152,167 55,174 1,94" fill="#0b0b0b"/>
    </svg>
    <div class="badge-text">
      <div class="badge-span">4-5</div>
      <div class="badge-unit">MONTHS</div>
      <div class="badge-month">NOV</div>
      <div class="badge-year">2025</div>
    </div>
  </div>

  <section class="courses">
    <article class="course course-1">
      <h2 class="course-title">Software,<br>Web &amp; Apps</h2>
      <p class="course-tag">&nbsp;# 2 Best Tech Job National Career Review 2025<small>Job Opportunities</small></p>
      <ul class="ticks">
        <li>Computer Programmer</li>
        <li>Software Developer / Mobile</li>
        <li>Engineer Developer (Apps)</li>
      </ul>
      <p class="optional"><strong>Optional:</strong><br>Bachelors in Prog. &amp; Tech</p>
      <p class="duration">NOV 2025</p>
    </article>
    <div class="course-divider" style="left:193px"></div>

    <article class="course course-2">
      <h2 class="course-title">Book-<br>keeping<br>LedgerPro</h2>
      <p class="course-tag">Train for a quality job Manage your own books</p>
      <ul class="ticks">
        <li>Finance<br>Management</li>
        <li>Customer &amp; Vendor Mgmt.</li>
        <li>Advanced Tools</li>
      </ul>
      <p class="duration">5 WEEKS<br>NOV&nbsp; 2025</p>
    </article>
    <div class="course-divider" style="left:397px"></div>

    <article class="course course-3">
      <h2 class="course-title">IT Desktop &amp;<br>Networking<br>Support</h2>
      <p class="course-tag">&nbsp;#2 Best Job<br>National Career Review 2025</p>
      <p class="course-note">&nbsp;Masters IT:</p>
      <ul class="ticks tight">
        <li>Panelo OS</li>
        <li>Networks</li>
        <li>Servers</li>
        <li>Cloud</li>
      </ul>
      <p class="duration">7 MONTHS<br>DEC 2025</p>
    </article>
    <div class="course-divider" style="left:601px"></div>

    <article class="course course-4">
      <h2 class="course-title">Northsoft<br>Office-<br>Computers</h2>
      <p class="course-tag">The New Job Prerequisite</p>
      <ul class="ticks">
        <li>Gridsheet</li>
        <li>Scribe</li>
        <li>Mailbox</li>
        <li>SlideDeck</li>
      </ul>
      <p class="lab">Computer lab<br>available to practice</p>
      <p class="duration">5 WEEKS<br>DEC 2025</p>
    </article>
  </section>

  <div class="rule" style="top:988px"></div>

  <footer class="closing">
    <p class="closing-kicker">SKILL UP, SALARY UP</p>
    <p class="closing-title">UPCOMING NVC COURSES</p>
    <p class="closing-facts"><span>MEN &amp; WOMEN</span><span>IN-PERSON &amp; REMOTE</span><span>PARTIAL SCHOLARSHIPS</span></p>
  </footer>

  <div class="rule" style="top:1105px"></div>
</main>
</body>
</html>
```